TRV Insurance - Letterhead

We need a corporate letterhead template (word) and slide show template (PowerPoint) designed for our Insurance Business.
TRV Insurance is in the insurance industry. Please visit our website www.trvinsurance-example.com
Both templates (word and PowerPoint) must include the TRV logo (attached to this project) and can be very similar in design.
We are after something creative yet professional in design.
Please feel free to ask any questions.

```html
<!DOCTYPE html>
<html lang="en">
<head>
<meta charset="utf-8">
<title>TRV Insurance – Letterhead</title>
<link href="https://fonts.googleapis.com/css2?family=Arimo:wght@400;700&display=swap" rel="stylesheet">
<style>
:root{
  --bg:#ece9e4;
  --paper:#ffffff;
  --ink:#111111;
  --muted:#555555;
  --rule:#9a9a9a;
  --rule-light:#cfcfcf;
  --red:#f0401c;
  --yellow:#f5e50c;
  --blue:#12148c;
  --swoosh:#e6e6e6;
  --faint:#e6f0f9;
}
*{box-sizing:border-box;margin:0;padding:0}
html,body{width:1200px;height:847px;overflow:hidden;background:var(--bg)}
body{font-family:"Arimo",Arial,sans-serif;color:var(--ink)}
.stage{position:relative;width:1200px;height:847px}
.sheet{position:absolute;background:var(--paper);box-shadow:0 2px 8px rgba(0,0,0,.18);overflow:hidden}
.sheet--cover{left:50px;top:32px;width:545px;height:720px}
.sheet--letter{left:612px;top:98px;width:550px;height:710px}
.swoosh{position:absolute;left:0;top:0}
.brand{position:absolute;font-family:"Arimo",Arial,sans-serif;font-weight:700;color:var(--ink);white-space:nowrap;line-height:1}
.brand--large{font-size:30px}
.brand--small{font-size:14px}
.tagline{position:absolute;font-size:8px;color:var(--muted);white-space:nowrap}
.contact{position:absolute;font-size:9.5px;line-height:1.2}
.contact li{list-style:none;display:flex;align-items:flex-start;gap:5px;margin-bottom:4px}
.icon{width:9px;height:9px;flex:none;margin-top:1px}
.rule{position:absolute;height:1px;background:var(--rule)}
.rule--light{background:var(--rule-light)}
.band{position:absolute;left:0;bottom:0;width:100%}
.envelope{position:absolute;background:var(--paper);box-shadow:1px 2px 4px rgba(0,0,0,.35);overflow:hidden}
.envelope--front{left:28px;top:160px;width:365px;height:160px}
.envelope--back{left:118px;top:335px;width:368px;height:200px}
.envelope__address{position:absolute;left:32px;top:60px;font-size:6px;line-height:1.3}
.handshake-area{position:absolute;border-radius:45%;background:radial-gradient(ellipse at center,var(--faint) 0%,rgba(230,240,249,0) 70%)}
.bars{position:absolute;right:32px;top:26px;font-size:7.5px;font-weight:700}
.bars li{list-style:none;display:flex;align-items:center;justify-content:flex-end;gap:3px;height:10px}
.bars i{display:block;height:6px}
.bars .b1{width:84px;background:linear-gradient(90deg,#f7b0a0,var(--red) 30%)}
.bars .b2{width:68px;margin-right:16px;background:linear-gradient(90deg,#faf3a8,var(--yellow) 30%)}
.bars .b3{width:46px;margin-right:38px;background:linear-gradient(90deg,#9a9bd0,var(--blue) 30%)}
.footer{position:absolute;left:58px;top:667px;display:flex;align-items:center;font-size:10.5px}
.footer span{display:flex;align-items:center;gap:5px}
.footer .sep{width:1px;height:14px;background:var(--red);margin:0 9px}
</style>
</head>
<body>
<main class="stage">

  <section class="sheet sheet--cover">
    <svg class="swoosh" width="140" height="110" viewBox="0 0 140 110" aria-hidden="true">
      <path d="M0 0H140C70 8 28 45 10 110H0Z" fill="var(--swoosh)"/>
    </svg>
    <p class="brand brand--large" style="left:12px;top:52px">TRV Insurance</p>
    <p class="tagline" style="left:12px;top:94px">Your NEEDS | Your INSURANCE | Your WAY</p>
    <ul class="contact" style="left:383px;top:42px">
      <li><svg class="icon" viewBox="0 0 10 10"><circle cx="5" cy="5" r="5"/><circle cx="5" cy="4" r="1.6" fill="#fff"/></svg><span>PO Box 418<br>Lakeside North, VIC 3190</span></li>
      <li><svg class="icon" viewBox="0 0 10 10"><circle cx="5" cy="5" r="5"/><rect x="3.5" y="2.5" width="3" height="5" rx=".6" fill="#fff"/></svg><span>1300 555 018</span></li>
      <li><svg class="icon" viewBox="0 0 10 10"><circle cx="5" cy="5" r="5"/><rect x="2.5" y="3.3" width="5" height="3.4" fill="#fff"/></svg><span>info@trvinsurance-example.com</span></li>
    </ul>
    <div class="rule" style="left:12px;top:108px;width:497px"></div>

    <div class="envelope envelope--front">
      <svg class="swoosh" width="90" height="70" viewBox="0 0 90 70" aria-hidden="true">
        <path d="M0 0H90C45 5 18 28 6 70H0Z" fill="var(--swoosh)"/>
      </svg>
      <p class="brand brand--small" style="left:30px;top:24px">TRV Insurance</p>
      <p class="tagline" style="left:32px;top:45px;font-size:4.5px">Your NEEDS | Your INSURANCE | Your WAY</p>
      <p class="envelope__address">PO Box 418<br>Lakeside North, VIC 3190</p>
      <svg class="band" height="8" viewBox="0 0 365 8" preserveAspectRatio="none" aria-hidden="true">
        <polygon points="0,0 150,0 142,8 0,8" fill="var(--red)"/>
        <polygon points="150,0 290,0 282,8 142,8" fill="var(--yellow)"/>
        <polygon points="290,0 365,0 365,8 282,8" fill="var(--blue)"/>
      </svg>
    </div>

    <div class="envelope envelope--back">
      <svg style="position:absolute;left:0;top:0" width="368" height="60" viewBox="0 0 368 60" aria-hidden="true">
        <polygon points="50,4 362,4 180,52" fill="var(--swoosh)"/>
        <polyline points="0,0 180,56 368,0" fill="none" stroke="#d8d8d8" stroke-width="1"/>
      </svg>
      <svg class="band" height="8" viewBox="0 0 368 8" preserveAspectRatio="none" aria-hidden="true">
        <polygon points="0,0 165,0 157,8 0,8" fill="var(--red)"/>
        <polygon points="165,0 300,0 292,8 157,8" fill="var(--yellow)"/>
        <polygon points="300,0 368,0 368,8 292,8" fill="var(--blue)"/>
      </svg>
    </div>

    <div class="handshake-area" role="img" aria-label="Faint handshake illustration" style="left:395px;top:580px;width:150px;height:110px"></div>
    <svg class="band" height="12" viewBox="0 0 545 12" preserveAspectRatio="none" aria-hidden="true">
      <polygon points="0,0 228,0 216,12 0,12" fill="var(--red)"/>
      <polygon points="228,0 452,0 440,12 216,12" fill="var(--yellow)"/>
      <polygon points="452,0 545,0 545,12 440,12" fill="var(--blue)"/>
    </svg>
  </section>

  <section class="sheet sheet--letter">
    <p class="brand brand--large" style="left:30px;top:40px">TRV Insurance</p>
    <ul class="bars">
      <li>Your NEEDS <i class="b1"></i></li>
      <li>Your INSURANCE <i class="b2"></i></li>
      <li>Your WAY <i class="b3"></i></li>
    </ul>
    <div class="rule rule--light" style="left:24px;top:82px;width:500px"></div>

    <div class="handshake-area" role="img" aria-label="Faint handshake illustration" style="left:395px;top:600px;width:150px;height:100px"></div>

    <div class="rule rule--light" style="left:24px;top:654px;width:500px"></div>
    <p class="footer">
      <span><svg class="icon" viewBox="0 0 10 10"><circle cx="5" cy="5" r="5"/><circle cx="5" cy="4" r="1.6" fill="#fff"/></svg>PO Box 418,&nbsp; Lakeside North, VIC 3190</span>
      <i class="sep"></i>
      <span><svg class="icon" viewBox="0 0 10 10"><circle cx="5" cy="5" r="5"/><rect x="3.5" y="2.5" width="3" height="5" rx=".6" fill="#fff"/></svg>1300 555 018</span>
      <i class="sep"></i>
      <span><svg class="icon" viewBox="0 0 10 10"><circle cx="5" cy="5" r="5"/><rect x="2.5" y="3.3" width="5" height="3.4" fill="#fff"/></svg>info@trvinsurance-example.com</span>
    </p>
  </section>

</main>
</body>
</html>
```